Business card - Brio Margin - size 85 mm * 55 mm

We need new business cards. Design must fit with our vision of the firm. You find in the attached file our logo and a short description of our firm (mission, vision, value, business and so on).

Target Market(s)

Consulting firm in performance improvement

Industry/Entity Type

Management Consulting

Contact Information for Business Card

SIZE
85 mm * 55 mm
INFORMATIONS
name surname
role position
telephone number
email address

Requirements
Must have
• the brand must APPEAR for the rest Would we like to have something sleek, inspired to a "just right" approach
Should not have
• Please avoid the black color as background

```html
<!DOCTYPE html>
<html lang="en">
<head>
<meta charset="utf-8">
<title>Brio Margin — Business Card</title>
<link href="https://fonts.googleapis.com/css2?family=Montserrat:wght@400;500;700&display=swap" rel="stylesheet">
<style>
  :root {
    --backdrop: #e9e6e2;
    --card-light: #ffffff;
    --card-dark: #414141;
    --brand-orange: #ee6a24;
    --text-grey: #6b6b6b;
    --faint-peach: #fbeee6;
    --faint-dark: #4a4645;
  }
  * { margin: 0; padding: 0; box-sizing: border-box; }
  html, body {
    width: 1200px; height: 1000px; overflow: hidden;
    background: var(--backdrop);
    font-family: "Montserrat", Arial, sans-serif;
  }
  .stage { position: relative; width: 1200px; height: 1000px; }
  .card {
    position: absolute; left: 265px; width: 665px; height: 397px;
    border-radius: 22px; overflow: hidden;
  }
  .card--front { top: 73px; background: var(--card-light); box-shadow: 0 6px 16px rgba(0,0,0,.18); }
  .card--back { top: 533px; background: var(--card-dark); box-shadow: 0 6px 16px rgba(0,0,0,.25); }
  .decor-ring { position: absolute; border-radius: 50%; }
  .card--front .decor-ring {
    left: 320px; top: 30px; width: 340px; height: 340px;
    border: 22px solid var(--faint-peach);
  }
  .card--back .decor-ring {
    left: -20px; top: -50px; width: 380px; height: 380px;
    border: 26px solid var(--faint-dark);
  }
  .brand-mark { position: absolute; border-radius: 50%; border: 5px solid var(--brand-orange); }
  .brand-name {
    position: absolute; color: var(--brand-orange); font-weight: 500;
    font-size: 20px; letter-spacing: 6px; white-space: nowrap;
  }
  .card--front .brand-mark { left: 96px; top: 40px; width: 96px; height: 96px; }
  .card--front .brand-name { left: 44px; top: 151px; }
  .card--back .brand-mark { left: 443px; top: 105px; width: 114px; height: 114px; }
  .card--back .brand-name { left: 374px; top: 246px; font-size: 21px; letter-spacing: 7px; }
  .person { position: absolute; right: 74px; top: 182px; text-align: right; }
  .person__name { color: var(--brand-orange); font-weight: 700; font-size: 18px; }
  .person__role { color: var(--text-grey); font-size: 14.5px; margin-top: 3px; }
  .address { position: absolute; left: 45px; top: 219px; color: var(--text-grey); font-size: 14.5px; line-height: 22px; }
  .contacts { position: absolute; left: 45px; top: 276px; list-style: none; color: var(--text-grey); font-size: 14.5px; }
  .contacts li { display: flex; align-items: center; height: 21px; }
  .contacts svg { width: 15px; height: 15px; margin-right: 8px; fill: var(--brand-orange); }
  .accent { color: var(--brand-orange); }
</style>
</head>
<body>
<div class="stage">
  <section class="card card--front">
    <div class="decor-ring" aria-hidden="true"></div>
    <div class="brand-mark" aria-hidden="true"></div>
    <div class="brand-name">BRIO MARGIN</div>
    <div class="person">
      <div class="person__name">DELIA MARCHETTI</div>
      <div class="person__role">Managing Director</div>
    </div>
    <address class="address" style="font-style:normal">
      Post Office Box 4410378<br>Covington, LA 70433
    </address>
    <ul class="contacts">
      <li><svg viewBox="0 0 16 16"><path d="M2 6c0-2 2-3 6-3s6 1 6 3v1h-3V6H5v1H2zM4 8h8l2 5H2z"/></svg>+ 000 000 0000 EXT 1</li>
      <li><svg viewBox="0 0 16 16"><path d="M4 2h8v3H4zM1 6h14v6h-3v-2H4v2H1zM5 11h6v3H5z"/></svg>+ 000 000 0000 EXT 1</li>
      <li><svg viewBox="0 0 16 16"><path d="M1 3h14v10H1zm1.5 1.5L8 9l5.5-4.5z" fill-rule="evenodd"/></svg>info@briomarginconsult.com</li>
      <li><svg viewBox="0 0 16 16"><circle cx="8" cy="8" r="6.5" fill="none" stroke="#ee6a24" stroke-width="2"/><path d="M7 6l7 4-3 1 2 3-1.5 1-2-3-2.5 2z"/></svg>www.<span class="accent">briomarginconsult</span>.com</li>
    </ul>
  </section>

  <section class="card card--back">
    <div class="decor-ring" aria-hidden="true"></div>
    <div class="brand-mark" aria-hidden="true"></div>
    <div class="brand-name">BRIO MARGIN</div>
  </section>
</div>
</body>
</html>
```